Management Consultancy needs sharp professional services showcased in a brochure

We are a management consultancy specializing on contract management and conflict avoidance services requiring a professional brochure showcasing our services to prospective clients.

Attached are a selection of existing stationary and the colour scheme.

Further details on our company can be found at www.velmor-advisory-partners.com
Updates

Preference is for bi-fold, however, innovative tri-fold will be considered. Added Monday, August 7, 2017

Target Market(s)

Construction companies, consultants, developers, oil and gas service providers, NGO's, SME's.

Industry/Entity Type

Management

Requirements
Must have
• High degree of professionalism with eye catching, sharp detail. No frils.
• Colour scheme as per the attachments
• Font as per attachments - Century Gothic
• Details of our company and services
Nice to have
• Open to ideas, thinking along the lines of a car brochure type design.
• Bi-fold preferred, by trifold accepted if innovative.
Should not have
• Remove reference to the United Arab Emirates.
• No cartoon/clipart photos.

```html
<!DOCTYPE html>
<html lang="en">
<head>
<meta charset="utf-8">
<title>Services Brochure – Inner Spread</title>
<link href="https://fonts.googleapis.com/css2?family=Questrial&family=Poppins:wght@500;600&display=swap" rel="stylesheet">
<style>
  :root {
    --navy: #15335a;
    --red: #b5161f;
    --ink: #3a3d44;
    --paper: #ffffff;
    --paper-shade: #f3f4f6;
    --backdrop: #dfe6ee;
    --rule: #15335a;
  }
  * { box-sizing: border-box; margin: 0; padding: 0; }
  html, body { width: 1200px; height: 900px; overflow: hidden; }
  body {
    background: var(--backdrop);
    font-family: "Questrial", "Century Gothic", sans-serif;
    color: var(--ink);
  }
  .spread {
    position: absolute;
    left: 33px; top: 17px;
    width: 1134px; height: 866px;
    display: grid;
    grid-template-columns: repeat(3, 1fr);
    border-top: 6px solid var(--rule);
    border-bottom: 6px solid var(--rule);
    background: var(--paper);
  }
  .panel {
    padding: 26px 28px 20px;
    font-size: 11.4px;
    line-height: 1.4;
    position: relative;
  }
  .panel + .panel { border-left: 1px solid #e2e4e8; }
  .panel--conflict { background: linear-gradient(100deg, #fff 0%, var(--paper-shade) 100%); }
  .panel-title {
    font-family: "Questrial", "Century Gothic", sans-serif;
    font-size: 25px;
    letter-spacing: 0.5px;
    color: var(--navy);
    margin: 6px 0 14px;
  }
  .panel p { margin-bottom: 7px; text-align: justify; }
  .service-title {
    font-family: "Poppins", "Century Gothic", sans-serif;
    font-weight: 600;
    font-size: 13px;
    line-height: 1.25;
    color: var(--red);
    margin: 12px 0 7px;
  }
  .panel--services { padding: 0; display: flex; flex-direction: column; }
  .services-intro {
    background: var(--navy);
    color: #eef2f7;
    padding: 26px 28px 26px;
    height: 515px;
  }
  .services-intro .panel-title { color: #fff; }
  .services-intro p { margin-bottom: 14px; }
  .site-address { font-size: 15px; color: #fff; margin-top: 24px; }
  .services-more { padding: 32px 28px 20px; }
  .services-more p { margin-bottom: 6px; text-align: left; }
</style>
</head>
<body>
<main class="spread">
  <section class="panel panel--conflict">
    <h2 class="panel-title">CONFLICT ADVISORY</h2>
    <p>Every conflict has the ability to be settled, it is on this premise we deliver effective solutions to contractual and commercial disputes with the aim of preserving the relationships and strengthening the parties for the future ahead.</p>

    <h3 class="service-title">Restoration and Mediation Services</h3>
    <p>Providing advocacy in the field of general commercial and contract issues, real estate, construction (property, civil engineering and vessel - ship and rig) and oilfield services (including aviation, chartering, medical services and purchase).</p>
    <p>Providing effective restoration methods, achieving a mutually acceptable outcome in all phases of the conflict cycle, ensuring that parties leave stronger, more committed and accountable for the progress of the transaction and relationship.</p>

    <h3 class="service-title">Shuttle Diplomacy and In Persona<br>Intermediary Services</h3>
    <p>Providing presence in disputes and processes where parties are:</p>
    <p>(a) unable to attend or<br>(b) unwilling to attend.</p>
    <p>Additionally providing a neutral platform for documentation submission review and filing, aiding vetting and response in shuttle diplomacy.</p>

    <h3 class="service-title">Negotiation Support Services</h3>
    <p>Ensuring success in negotiation, we aim to provide direction in negotiation in the early stages of conflict in order to avert escalation and to reduce conflict aftermath.</p>
    <p>Through assessment of relationship, perception and conflict strategy we ensure adequate negotiation preparation and guidance with the increased outcome of a win win for all parties.</p>

    <h3 class="service-title">Workplace / Corporate Mediation Services</h3>
    <p>Providing effective resolution to workplace misunderstandings, personality conflicts, co-operation and opinion differences, with the objective of increasing workplace performance, and reducing management and HR resource displacement.</p>
  </section>

  <section class="panel panel--contract">
    <h2 class="panel-title">CONTRACT ADVISORY</h2>
    <p>Effective contract management delivered through our Contract Advisory ensures that the contract is as effective as it can be. Through review, planning and effective application, we ensure that contractual obligations are maintained and risks are mitigated through the full contract life cycle providing the optimum contractual engagement.</p>

    <h3 class="service-title">Contract Troubleshooting</h3>
    <p>Contract Troubleshooting including drafting and interpretation assistance via our "Second Set" protocol.</p>
    <p>Providing secondary review, analysis and interpretation with reporting on application of clauses including layman dissection aiding the deconstruction of terms to reveal the true meaning and implications.</p>
    <p>Contract Workshops with key stakeholders enabling a harmonised understanding of contractual obligations enabling clear procedure establishment.</p>

    <h3 class="service-title">Tender Review &amp; Bid Support</h3>
    <p>Guidance in tender review both recieved and issued RFQ and RFP drafting and review.</p>

    <h3 class="service-title">Contracts Audit Services &amp;<br>Performance Management</h3>
    <p>Audit of contractual mechanisms, compliance and corrective reviews on deficiencies.</p>
    <p>Advisory and guidance for corrective measures including performance management and establishment and monitoring of Key performance Inidcators ("KPI's").</p>
    <p>Contract harmonisation and benchmarking.</p>
    <p>Post contract maintenance and administration guidance and contract management planning. Third party contract audit including Project Management Consultancy ("PMC")/ PRoject Management Team ("PMT") process review for major and minor projects.</p>

    <h3 class="service-title">Contract Fraud Investigation</h3>
    <p>Advisory of contract practices which are susceptible to fraudulent activity and investigation of key areas where fraud is suspected.</p>
  </section>

  <section class="panel panel--services">
    <div class="services-intro">
      <h2 class="panel-title">OUR SERVICES</h2>
      <p>Every contract has at least two parties; every party has a goal, and every goal matters. Each party must work in equilibrium as a contractual partnership or alliance, it is on this premise we aim to deliver truly mutual agreements, maintaining the contract integrity from inception through the contract life, and where we are not party to the original agreement, we provide effective solutions to contractual conflict via our unique mediation methodology at all positions of the conflict cycle and aim to enhance all aspects of contract performance by effective audit and management.</p>
      <p>We believe that a proactive approach to contract management creates transparency and trust, and maintains relationships and builds on them for the future whilst cultivating significant value to your business transactions and addressing real and relevant issues, providing and implementing effective solutions. We believe that avoidance of contractual conflict and timely resolution on escalation is paramount in the effectiveness of any agreement.</p>
      <p class="site-address">www.velmor-advisory-partners.com</p>
    </div>
    <div class="services-more">
      <h3 class="service-title">Strategic Review &amp; Contract Risk Assessment</h3>
      <p>Advisory of current contract application suitability.</p>
      <p>Steering guidance and contract assessment advisory</p>
      <p>Contractual risk and optimization assessments.</p>
      <p>Development of internal contract management and administration policy and procedure.</p>
      <p>Contract management planning – Advisory at all phases of the contract Life Cycle ("CLC").</p>

      <h3 class="service-title">Temporary Placement Contract<br>Management Solutions</h3>
      <p>Provision of fixed term temporary contract management and contracts administration professionals into your organisation to provide immediate on hand contracts management solutions.</p>
    </div>
  </section>
</main>
</body>
</html>
```